Unique business card design

Boutique coastal hotel suites - in need of clever stand out business card I have uploaded the logo that I had created through brand loft I want something that is clever and stands out from everyone else - 418 Marrowind Lane seldovia Alaska 99528 phone or text 907 -561-8204 www.tidewrenlodgeinn.com

Target Market(s)

Men and woman

Industry/Entity Type

Boutique coastal hotel

Contact Information for Business Card

Tidewren Lodge Harrowick Alaska tidewren_lodge@kelpmail.com

Requirements
Must have
• Classy - clever -bold 907-561-8204 call or text

```html
<!DOCTYPE html>
<html lang="en">
<head>
<meta charset="utf-8">
<title>Tidewren Lodge — Business Card</title>
<link rel="stylesheet" href="https://fonts.googleapis.com/css2?family=Montserrat:wght@500;600;700&family=Arimo:wght@400&display=swap">
<style>
  :root {
    --stage: #d9d9d9;
    --paper: #efebe4;
    --navy: #2f4f70;
    --red: #d02a2a;
    --yellow: #f2d34a;
    --charcoal: #2b2b2b;
    --ink: #3a3a3a;
    --white: #ffffff;
  }
  * { box-sizing: border-box; margin: 0; padding: 0; }
  html, body { width: 1200px; height: 900px; overflow: hidden; }
  body {
    background: var(--stage);
    font-family: "Arimo", Arial, sans-serif;
    position: relative;
  }
  .card {
    position: absolute;
    left: 260px;
    width: 680px;
    height: 388px;
    background: var(--paper);
    box-shadow: 0 6px 18px rgba(0,0,0,0.18);
    overflow: hidden;
  }
  .card--front { top: 46px; }
  .card--back { top: 466px; }

  /* front */
  .flag-cluster { position: absolute; height: 62px; }
  .flag-cluster--top-left {
    top: 0; left: 0; width: 170px;
    background: linear-gradient(90deg, var(--white) 0 50%, var(--navy) 50% 75%, var(--red) 75%);
  }
  .flag-cluster--top-right {
    top: 0; right: 0; width: 170px;
    background: linear-gradient(90deg, var(--yellow) 0 25%, var(--charcoal) 25% 50%, var(--navy) 50% 85%, var(--yellow) 85%);
  }
  .flag-cluster--bottom-left {
    bottom: 0; left: 0; width: 180px;
    background: linear-gradient(90deg, var(--red) 0 25%, var(--yellow) 25% 50%, var(--white) 50% 80%, var(--red) 80%);
  }
  .flag-cluster--bottom-right {
    bottom: 70px; right: 0; width: 170px;
    background: linear-gradient(90deg, var(--yellow) 0 50%, var(--white) 50% 68%, var(--navy) 68%);
  }
  .brand {
    position: absolute;
    left: 0; right: 0;
    text-align: center;
    font-family: "Montserrat", Arial, sans-serif;
    font-weight: 600;
    color: var(--navy);
    letter-spacing: 0.08em;
    text-transform: uppercase;
    white-space: nowrap;
  }
  .card--front .brand { top: 160px; font-size: 46px; }

  /* back */
  .card--back .brand { top: 34px; font-size: 32px; }
  .brand-rule {
    position: absolute;
    top: 96px; left: 215px;
    width: 250px; height: 2px;
    background: var(--charcoal);
  }
  .person {
    position: absolute;
    top: 246px; left: 150px;
    text-align: right;
    font-family: "Montserrat", Arial, sans-serif;
  }
  .person__name { font-size: 27px; font-weight: 700; color: var(--navy); white-space: nowrap; }
  .person__role { font-size: 13px; font-weight: 500; color: var(--ink); margin-top: -2px; }
  .divider {
    position: absolute;
    top: 132px; left: 380px;
    width: 3px; height: 200px;
    background: var(--red);
  }
  .contact {
    position: absolute;
    top: 144px; left: 414px;
    font-size: 15px;
    color: var(--ink);
    line-height: 1.45;
    white-space: nowrap;
  }
  .contact__address { margin-bottom: 22px; }
  .contact__list { list-style: none; }
  .contact__item { display: flex; align-items: center; gap: 10px; }
  .contact__icon { width: 14px; height: 14px; fill: var(--navy); flex: none; }
</style>
</head>
<body>
  <section class="card card--front" aria-label="Card front">
    <div class="flag-cluster flag-cluster--top-left" role="img" aria-label="Nautical signal flag decoration"></div>
    <div class="flag-cluster flag-cluster--top-right" role="img" aria-label="Nautical signal flag decoration"></div>
    <div class="flag-cluster flag-cluster--bottom-right" role="img" aria-label="Nautical signal flag decoration"></div>
    <div class="flag-cluster flag-cluster--bottom-left" role="img" aria-label="Nautical signal flag decoration"></div>
    <p class="brand">Tidewren Lodge</p>
  </section>

  <section class="card card--back" aria-label="Card back">
    <p class="brand">Tidewren Lodge</p>
    <div class="brand-rule"></div>

    <div class="person">
      <p class="person__name">Marla Ostby</p>
      <p class="person__role">Director</p>
    </div>

    <div class="divider"></div>

    <div class="contact">
      <p class="contact__address">418 Marrowind Lane<br>Harrowick Alaska 99528</p>
      <ul class="contact__list">
        <li class="contact__item">
          <svg class="contact__icon" viewBox="0 0 24 24" aria-hidden="true"><path d="M6.6 10.8a15.1 15.1 0 0 0 6.6 6.6l2.2-2.2a1 1 0 0 1 1-.25 11.4 11.4 0 0 0 3.6.57 1 1 0 0 1 1 1V20a1 1 0 0 1-1 1A17 17 0 0 1 3 4a1 1 0 0 1 1-1h3.5a1 1 0 0 1 1 1c0 1.250.2 2.45.57 3.57a1 1 0 0 1-.25 1z"/></svg>
          <span>907 561 8204</span>
        </li>
        <li class="contact__item">
          <svg class="contact__icon" viewBox="0 0 24 24" aria-hidden="true"><path d="M2 5h20v14H2zm2 2v.5l8 5 8-5V7zm0 2.9V17h16V9.9l-8 5z"/></svg>
          <span>tidewren_lodge@kelpmail.com</span>
        </li>
        <li class="contact__item">
          <svg class="contact__icon" viewBox="0 0 24 24" aria-hidden="true"><circle cx="12" cy="12" r="10"/></svg>
          <span>www.tidewrenlodgeinn.com</span>
        </li>
      </ul>
    </div>
  </section>
</body>
</html>
```